Website Design for my CNC machine Shop.

I need a new website for my Machining Company.

It can be a simple website that acts more like an "Online Business card" I has to highlight the services I provide and give Companies the confidence to engage my services.

I needs it to be a really modern or even a little futuristic promoting my Company.

I have just moved locations and have renovated the premises and would be great to let everyone know along with a new website.

If you can help with linking it to search engines to help get more exposure that would be great.

It needs to accommodate the three main services I provide which will include capacities of each machine (within that service) and maybe a couple images.
CNC Machining (5-axis, 3-axis)
EDM Wire cutting
3D Metal Printing
Along with home page and Contact page

I have two websites and you can use the txt from either/combination of these.
www.korvaltooling.com.au
(no longer do Laser Marking and etching but now do 3D metal Printing)
www.tarnquill.com.au

Happy to chat further with the designer

Company logo's provided.

For Images: I am happy to use Glimmerbay and can purchase any images you like
EDM Wire cut
https://www.glimmerbay-pics.com/search/edm-wire-cutting

CNC Machining:
https://www.glimmerbay-pics.com/search/vertical-cnc-machining
Don't use any with engines or motor vehicle parts

3D metal Printing
https://www.glimmerbay-pics.com/search/slm-metal-printing

Target Market(s)

Defence, Aerospace, Medical, HIgh Precision

Industry/Entity Type

Mechanical Engineering

Coding

Coded - Design and coding required

Number of Pages Required

5+ page

Requirements
Must have
• Home page, 3 services, Contacts. Can add image to each of the services

```html
<!DOCTYPE html>
<html lang="en">
<head>
<meta charset="utf-8">
<title>KORVAL Precision Machinists</title>
<link href="https://fonts.googleapis.com/css2?family=Poppins:wght@300;400;500;600&display=swap" rel="stylesheet">
<style>
:root{
  --navy:#062a3a;
  --green:#37b98a;
  --ink:#0d2633;
  --muted:#6f7b80;
  --white:#ffffff;
  --rule:#cfd6d8;
}
*{box-sizing:border-box;margin:0;padding:0}
html,body{width:1200px;height:826px;overflow:hidden;background:var(--white);font-family:'Poppins',sans-serif;color:var(--ink)}
.topbar{height:42px;background:var(--navy);display:flex;align-items:center;justify-content:space-between;padding:0 100px;color:var(--white);font-size:10.5px}
.contact-list{display:flex;align-items:center}
.contact-item{display:flex;align-items:center;gap:5px;padding:0 9px;border-right:1px solid var(--white);line-height:20px}
.contact-item:first-child{padding-left:0}
.contact-item:last-child{border-right:none}
.contact-item svg{fill:var(--green)}
.social{display:flex;gap:9px}
.social span{width:17px;height:17px;border-radius:3px;background:var(--green);display:block}
.site-header{height:66px;display:flex;align-items:center;justify-content:space-between;padding:0 100px}
.brand{display:flex;flex-direction:column}
.brand-name{font-size:33px;font-weight:500;letter-spacing:5px;color:var(--navy);line-height:34px}
.brand-tag{font-size:7.5px;letter-spacing:2.4px;color:var(--green);margin-top:2px}
.main-nav{display:flex;gap:25px;font-size:14px}
.main-nav a{color:var(--ink);text-decoration:none}
.main-nav a.active{color:var(--green)}
.hero{height:151px;background:var(--green);text-align:center;padding-top:34px}
.hero h1{font-size:25px;font-weight:600;color:var(--white);line-height:30px}
.hero p{width:800px;margin:19px auto 0;font-size:12.3px;line-height:17.5px;color:var(--ink)}
.services{display:flex;justify-content:space-between;padding:39px 100px 0}
.card{width:292px;height:417px;background:var(--white);border-radius:14px;box-shadow:0 2px 14px rgba(0,0,0,.12);padding:21px;display:flex;flex-direction:column;align-items:center}
.card-photo{width:250px;height:178px;border-radius:7px}
.photo-cnc{background:linear-gradient(135deg,#4a4f54,#a9aeb2 45%,#2a2d30)}
.photo-edm{background:linear-gradient(160deg,#2b3440,#8b8f92 50%,#c9b79c 60%,#1f2327)}
.photo-print{background:linear-gradient(180deg,#d7d9d8,#a9abab 60%,#6c6f70)}
.card h2{font-size:21.5px;font-weight:500;color:var(--green);margin-top:11px;line-height:28px}
.card-rule{width:250px;height:1px;background:var(--rule);position:relative;margin-top:6px}
.card-rule::after{content:"";position:absolute;left:50%;transform:translateX(-50%);top:-1px;width:160px;height:3px;background:var(--green)}
.card p{width:250px;margin-top:17px;font-size:11.2px;line-height:16.7px;color:var(--muted);font-weight:300;text-align:justify;flex:1}
.btn{background:var(--green);color:var(--white);font-size:13.5px;border-radius:5px;padding:3px 16px;text-decoration:none;margin-bottom:4px}
.site-footer{position:absolute;top:757px;left:0;width:1200px;height:69px;background:var(--navy);text-align:center;padding-top:14px}
.footer-nav{display:flex;justify-content:center;font-size:10.5px}
.footer-nav a{color:var(--green);text-decoration:none;padding:0 8px;border-right:1px solid var(--white);line-height:14px}
.footer-nav a:last-child{border-right:none}
.copyright{color:var(--white);font-size:10px;margin-top:12px}
</style>
</head>
<body>
<div class="topbar">
  <div class="contact-list">
    <span class="contact-item"><svg width="14" height="14" viewBox="0 0 24 24"><path d="M6.6 10.8a15 15 0 006.6 6.6l2.2-2.2a1 1 0 011-.25 11.4 11.4 0 003.6.57 1 1 0 011 1V20a1 1 0 01-1 1A17 17 0 013 4a1 1 0 011-1h3.5a1 1 0 011 1c0 1.25.2 2.45.57 3.57a1 1 0 01-.25 1z"/></svg>Mob +61 400 555 018</span>
    <span class="contact-item"><svg width="16" height="12" viewBox="0 0 24 18"><path d="M0 0h24v18H0z M2 2l10 8 10-8" stroke="#062a3a" stroke-width="1.6"/></svg>info@korvaltooling.com.au</span>
    <span class="contact-item"><svg width="12" height="16" viewBox="0 0 24 32"><path d="M12 0C5.4 0 0 5.4 0 12c0 9 12 20 12 20s12-11 12-20C24 5.4 18.6 0 12 0zm0 17a5 5 0 110-10 5 5 0 010 10z"/></svg>Unit 4, 18 Brindle Park rd, ASHVALE, VIC 3999</span>
  </div>
  <div class="social" aria-label="Social links"><span></span><span></span><span></span><span></span></div>
</div>
<header class="site-header">
  <div class="brand"><span class="brand-name">KORVAL</span><span class="brand-tag">PRECISION MACHINISTS</span></div>
  <nav class="main-nav"><a class="active" href="#">Home</a><a href="#">CNC Machining</a><a href="#">EDM Wire cutting</a><a href="#">3D Metal Printing</a><a href="#">Contact Us</a></nav>
</header>
<section class="hero">
  <h1>We are an innovative&nbsp; company that specialise in technical and creative engineering</h1>
  <p>Our core sectors of expertise are in EDM wire cutting, 3D Metal Printing and CNC machining. With our combination of highly skilled staff and sophisticated machinery we offer a comprehensive and professional service.</p>
</section>
<main class="services">
  <article class="card">
    <div class="card-photo photo-cnc" role="img" aria-label="Vertical CNC milling machine cutting metal with coolant spray"></div>
    <h2>CNC Machining</h2><div class="card-rule"></div>
    <p>With our combination of high quality Hexmoor Machining Centres we are able to provide innovative solutions to your precision CNC machining requirements.</p>
    <a class="btn" href="#">Learn More</a>
  </article>
  <article class="card">
    <div class="card-photo photo-edm" role="img" aria-label="EDM wire cutting machine sparking through a metal block"></div>
    <h2>EDM Wire cutting</h2><div class="card-rule"></div>
    <p>We operate Swiss manufactured Veltrane EDM Machines which are regarded as the Bentmore of wire cut machines.</p>
    <a class="btn" href="#">Learn More</a>
  </article>
  <article class="card">
    <div class="card-photo photo-print" role="img" aria-label="Laser nozzle of a metal 3D printer fusing powder"></div>
    <h2>3D Metal Printing</h2><div class="card-rule"></div>
    <p>With our combination of high quality Hexmoor Machining Centres we are able to provide innovative solutions to your precision CNC machining requirements.</p>
    <a class="btn" href="#">Learn More</a>
  </article>
</main>
<footer class="site-footer">
  <nav class="footer-nav"><a href="#">Home</a><a href="#">CNC Machining</a><a href="#">EDM Wire cutting</a><a href="#">3D Metal Printing</a><a href="#">Contact Us</a></nav>
  <p class="copyright">© 2014 by KORVAL</p>
</footer>
</body>
</html>
```